Mt Brindlewood Hotel

We need a business card with old world charm.
The design will need to promote dining and accommodation for local residents as a place to relax and for vacationing or week-end visitors seeking an experience of country hospitality.
The hotel was originally opened in 1909.

Target Market(s)

Adults and Families searching for dining and accommodation.

Industry/Entity Type

Business

Requirements
Nice to have
• Sketch or line drawing of Hotel

```html
<!DOCTYPE html>
<html lang="en">
<head>
<meta charset="utf-8">
<title>Mt Brindlewood Hotel – Business Card Concept</title>
<link rel="stylesheet" href="https://fonts.googleapis.com/css2?family=Federant&family=Josefin+Sans:wght@300;400&display=swap">
<style>
  :root {
    --page: #fbf6ec;
    --heading: #2a2623;
    --ink: #1e1a17;
    --card-light: #f8f0dc;
    --card-mid: #ecdfc0;
    --card-edge: #d6c297;
    --art-light: #e9dcbd;
    --art-dark: #b9a67e;
  }
  * { box-sizing: border-box; margin: 0; padding: 0; }
  html, body { width: 1200px; height: 2235px; overflow: hidden; }
  body {
    position: relative;
    background: var(--page);
    color: var(--heading);
    font-family: "Josefin Sans", sans-serif;
  }
  .page-title {
    position: absolute; left: 40px; top: 42px;
    font-weight: 400; font-size: 70px; letter-spacing: 4px; line-height: 1;
  }
  .page-subtitle {
    position: absolute; left: 40px; top: 132px;
    font-weight: 300; font-size: 54px; letter-spacing: 4px; line-height: 1;
  }
  .side-label {
    position: absolute; left: 44px;
    font-weight: 300; font-size: 56px; letter-spacing: 3px; line-height: 1;
  }
  .side-label--verso { top: 275px; }
  .side-label--front { top: 1178px; }

  .card {
    position: absolute; left: 42px; width: 1110px; height: 718px;
    background: radial-gradient(ellipse at 50% 45%, var(--card-light) 0%, var(--card-mid) 65%, var(--card-edge) 100%);
    box-shadow: 3px 6px 10px rgba(60, 45, 20, 0.28);
    color: var(--ink);
    font-family: "Federant", serif;
    overflow: hidden;
  }
  .card--verso { top: 342px; }
  .card--front { top: 1252px; }

  .card-frame { position: absolute; inset: 0; width: 1110px; height: 718px; }
  .card-frame line { stroke: var(--ink); stroke-linecap: round; }

  .corner-ornament {
    position: absolute; width: 105px; height: 105px; border-radius: 50%;
    background: radial-gradient(circle, var(--art-dark) 0%, var(--art-light) 75%, transparent 100%);
  }
  .corner-ornament--tl { left: 14px; top: 14px; }
  .corner-ornament--tr { right: 14px; top: 14px; }
  .corner-ornament--bl { left: 14px; bottom: 14px; }
  .corner-ornament--br { right: 14px; bottom: 14px; }

  .hotel-sketch {
    position: absolute;
    background: linear-gradient(180deg, var(--art-light), var(--art-dark));
  }
  .card--verso .hotel-sketch { left: 195px; top: 100px; width: 702px; height: 335px; }
  .card--front .hotel-sketch { left: 135px; top: 80px; width: 303px; height: 145px; }

  .hotel-name { position: absolute; text-align: center; white-space: nowrap; line-height: 1; font-weight: 400; }
  .card--verso .hotel-name { left: 138px; width: 810px; top: 476px; font-size: 64px; }
  .card--front .hotel-name { left: 114px; width: 346px; top: 242px; font-size: 28px; }

  .contact {
    position: absolute; right: 160px; top: 110px;
    text-align: right; font-size: 27px; line-height: 41px; letter-spacing: 1px;
    font-style: normal;
  }
  .person-name {
    position: absolute; right: 160px; top: 358px;
    font-size: 82px; line-height: 1; white-space: nowrap;
  }
  .person-role {
    position: absolute; left: 366px; top: 490px;
    font-size: 36px; letter-spacing: 2px; line-height: 1;
  }
  .person-phone {
    position: absolute; right: 160px; top: 544px;
    font-size: 56px; letter-spacing: 3px; line-height: 1;
  }
</style>
</head>
<body>
  <h1 class="page-title">Mt Brindlewood Hotel</h1>
  <p class="page-subtitle">Business Card Concept</p>

  <h2 class="side-label side-label--verso">Verso</h2>
  <section class="card card--verso">
    <svg class="card-frame" viewBox="0 0 1110 718" aria-hidden="true">
      <line x1="243" y1="21" x2="963" y2="21" stroke-width="2.5"/>
      <line x1="138" y1="36" x2="978" y2="36" stroke-width="4"/>
      <line x1="243" y1="697" x2="963" y2="697" stroke-width="2.5"/>
      <line x1="138" y1="682" x2="978" y2="682" stroke-width="4"/>
      <line x1="28" y1="138" x2="28" y2="588" stroke-width="2.5"/>
      <line x1="45" y1="150" x2="45" y2="560" stroke-width="4"/>
      <line x1="1082" y1="138" x2="1082" y2="588" stroke-width="2.5"/>
      <line x1="1065" y1="150" x2="1065" y2="560" stroke-width="4"/>
    </svg>
    <div class="corner-ornament corner-ornament--tl" role="img" aria-label="Scrolled corner flourish ornament"></div>
    <div class="corner-ornament corner-ornament--tr" role="img" aria-label="Scrolled corner flourish ornament"></div>
    <div class="corner-ornament corner-ornament--bl" role="img" aria-label="Scrolled corner flourish ornament"></div>
    <div class="corner-ornament corner-ornament--br" role="img" aria-label="Scrolled corner flourish ornament"></div>
    <div class="hotel-sketch" role="img" aria-label="Line drawing of the two-storey hotel building with gabled roofs and chimneys"></div>
    <p class="hotel-name">Mt Brindlewood Hotel</p>
  </section>

  <h2 class="side-label side-label--front">Front</h2>
  <section class="card card--front">
    <svg class="card-frame" viewBox="0 0 1110 718" aria-hidden="true">
      <line x1="243" y1="21" x2="963" y2="21" stroke-width="2.5"/>
      <line x1="138" y1="36" x2="978" y2="36" stroke-width="4"/>
      <line x1="243" y1="697" x2="963" y2="697" stroke-width="2.5"/>
      <line x1="138" y1="682" x2="978" y2="682" stroke-width="4"/>
      <line x1="28" y1="138" x2="28" y2="588" stroke-width="2.5"/>
      <line x1="45" y1="150" x2="45" y2="560" stroke-width="4"/>
      <line x1="1082" y1="138" x2="1082" y2="588" stroke-width="2.5"/>
      <line x1="1065" y1="150" x2="1065" y2="560" stroke-width="4"/>
    </svg>
    <div class="corner-ornament corner-ornament--tl" role="img" aria-label="Scrolled corner flourish ornament"></div>
    <div class="corner-ornament corner-ornament--tr" role="img" aria-label="Scrolled corner flourish ornament"></div>
    <div class="corner-ornament corner-ornament--bl" role="img" aria-label="Scrolled corner flourish ornament"></div>
    <div class="corner-ornament corner-ornament--br" role="img" aria-label="Scrolled corner flourish ornament"></div>
    <div class="hotel-sketch" role="img" aria-label="Small line drawing of the hotel building"></div>
    <p class="hotel-name">Mt Brindlewood Hotel</p>
    <address class="contact">
      Your Address<br>
      Zip, City<br>
      Tel/Fax<br>
      email/website
    </address>
    <p class="person-name">Marco Fellerini</p>
    <p class="person-role">Your Position</p>
    <p class="person-phone">+00 1234567</p>
  </section>
</body>
</html>
```